Gestaltung eines Bieretiketts gesucht
Zielgruppe
Wir sind eine Numetal Band und möchten an unsere Freunde,Fans und Weggefährten ein kleines individuelles Give Away in Form von Bier abgeben. Dazu benötigen wir ein Bieretikette.
+++Aufgrund eines kurzfristig Auslandsaufenthalt, kann keine Bewertung der Designvorschläge bis zum Ende der Laufzeit abgegeben werden. Am Samstag, 06.02.16 erfolgt die Ermittlung des Gewinndesigns. Sorry & Danke für das Verständnis.+++
Aufgabenstellung
Als Give Away möchten wir Bierflaschen mit einem individuellen Etiketten-Design verteilen. Wir stellen uns das Etikett wie die bekannten Bieretiketten vor. Die Vorderseite des Designs könnte einen Gerstenkranz, ein Hopfenbild oder einen Lorbeerkranz aufzeigen. Wir könnten uns aber auch vorstellen, dass nur der Name quer, waagerecht oder senkrecht dargestellt wird. Der Fantasie sind keine Grenzen gesetzt.
Die Rückseite wäre mit folgenden Infos zu versehen:
www.rustyfoxmoon.example
Wieselquellbräu, Moosbergen, Alpenland
0,33l
Alc. 4.5% Vol
Hals: Ein kleines Etikette
Die Schrift wäre: Impact
Anhang:
Darin enthalten die Schriftart, sowie die Farbkennung. Der Logoschriftzug muss nicht zwingend grün sein, sondern kann auch weiss od. schwarz sein.
Wenn Verwendung dafür können diese Utensilien gerne verwendet werden
Hierbei handelt es sich um das runde Bandlogo.
Dies soll unsere benötigen Etiketten darstellen (Vorne, hinten, Hals).
Gerne stehen wir für weitere Fragen zur Verfügung.

```html
<!DOCTYPE html>
<html lang="de">
<head>
<meta charset="utf-8">
<title>KVT – Bieretiketten</title>
<link rel="stylesheet" href="https://fonts.googleapis.com/css2?family=Anton&family=Oswald:wght@600&display=swap">
<style>
  :root {
    --label-black: #1d1d1b;
    --band-green: #1f9a3a;
    --label-white: #f4f4f2;
    --page-bg: #ffffff;
  }
  html, body {
    margin: 0;
    padding: 0;
    overflow: hidden;
  }
  .sheet {
    position: relative;
    width: 1200px;
    height: 4062px;
    background: var(--page-bg);
    overflow: hidden;
  }
  .neck-label {
    position: absolute;
    left: 315px;
    top: 115px;
    width: 572px;
    height: 284px;
    background: var(--label-black);
    display: flex;
    align-items: center;
    justify-content: center;
    gap: 22px;
  }
  .neck-label__dot {
    width: 54px;
    height: 54px;
    border-radius: 50%;
    background: var(--band-green);
  }
  .neck-label__name {
    font-family: "Anton", Impact, sans-serif;
    font-size: 84px;
    line-height: 1;
    color: var(--band-green);
    letter-spacing: 4px;
  }
  .front-label {
    position: absolute;
    left: 397px;
    top: 484px;
    width: 404px;
    height: 981px;
    background: var(--label-black);
  }
  .front-label svg {
    display: block;
  }
  .wordmark {
    font-family: "Anton", Impact, sans-serif;
    fill: var(--band-green);
  }
  .tagline {
    font-family: "Anton", Impact, sans-serif;
    fill: var(--label-white);
  }
  .brewery-info {
    font-family: "Oswald", Impact, sans-serif;
    font-weight: 600;
    font-size: 18px;
    fill: var(--band-green);
    letter-spacing: 1px;
  }
  .volume-info {
    font-family: "Anton", Impact, sans-serif;
    font-size: 29px;
    fill: var(--label-white);
  }
</style>
</head>
<body>
<main class="sheet">
  <section class="neck-label" aria-label="Halsetikett">
    <span class="neck-label__dot"></span>
    <span class="neck-label__name">KVT</span>
  </section>

  <section class="front-label" aria-label="Frontetikett">
    <svg width="404" height="981" viewBox="0 0 404 981" xmlns="http://www.w3.org/2000/svg">
      <text class="wordmark" transform="translate(144,757) rotate(-90)" font-size="84" textLength="692" lengthAdjust="spacingAndGlyphs">KITEVELVET</text>
      <text class="wordmark" transform="translate(262,757) rotate(-90)" font-size="122" textLength="692" lengthAdjust="spacingAndGlyphs">TAWNY</text>
      <text class="tagline" transform="translate(338,754) rotate(-90)" font-size="53" textLength="688" lengthAdjust="spacingAndGlyphs">BEER FOR BITCHES</text>

      <text class="brewery-info" x="71" y="837">WWW.RUSTYFOXMOON.EXAMPLE</text>
      <text class="brewery-info" x="71" y="864">WIESELQUELLBRÄU,</text>
      <text class="brewery-info" x="71" y="891">MOOSBERGEN, ALPENLAND</text>

      <text class="volume-info" x="69" y="940">Alc. 4.5% Vol</text>
      <text class="volume-info" x="286" y="940">0,33l</text>
    </svg>
  </section>
</main>
</body>
</html>
```